Family Ranch with a hobby vineyard needs 2 wine labels for our first harvest

Design 2 wine labels (front and back) with the Brindor Ranch logo.
Label 1:
Sauvignon Blanc
Alc. 12.5% by Vol.
Palos Verdes Peninsula - add as the region
Year 2022
Label 2:
Cabernet Sauvignon
Alc. 13.5% by Vol.
Year 2022
For the back label design:
GOVERNMENT WARNING: (1) According to the Surgeon General, women
should not drink alcoholic beverages during pregnancy because of the risk of
birth defects. (2) Consumption of alcoholic beverages impairs your ability to
drive a car or operate machinery, and may cause health problems.
Contains Sulfates.
750ML
I just received the bottles and have attached a picture.
Look and feel
Each slider illustrates characteristics of the customer's brand and the style your logo design should communicate.

```html
<!DOCTYPE html>
<html lang="en">
<head>
<meta charset="utf-8">
<title>Brindor Ranch – Wine Label Presentation, Draft 1</title>
<link rel="stylesheet" href="https://fonts.googleapis.com/css2?family=Montserrat:wght@400;500;600&family=EB+Garamond:wght@400;500&family=Great+Vibes&family=Roboto+Condensed:wght@400;700&family=Arimo&display=swap">
<style>
  :root {
    --paper: #ffffff;
    --ink: #1d1d1d;
    --rule: #333333;
    --band: #000000;

    --silver-fill: #8f9197;
    --silver-ink: #2c2d30;
    --silver-frame-a: #0c0c0d;
    --silver-frame-b: #c9cacd;
    --silver-frame-c: #3a3b3e;

    --gold-fill: #8f7a33;
    --gold-ink: #3f3212;
    --gold-frame-a: #4a3c10;
    --gold-frame-b: #d9c06a;
    --gold-frame-c: #6a5618;
    --gold-heading: #5a4a14;

    --sans: "Montserrat", "Arimo", sans-serif;
    --serif: "EB Garamond", Georgia, serif;
    --script: "Great Vibes", cursive;
    --condensed: "Roboto Condensed", "Arial Narrow", sans-serif;
    --plain: "Arimo", Arial, sans-serif;
  }

  * { box-sizing: border-box; margin: 0; padding: 0; }

  html, body {
    width: 750px;
    height: 1200px;
    overflow: hidden;
    background: var(--paper);
  }

  .sheet {
    position: relative;
    width: 750px;
    height: 1200px;
    background: var(--paper);
    color: var(--ink);
    font-family: var(--plain);
  }

  .variety-title {
    position: absolute;
    font-family: var(--plain);
    font-size: 10.5px;
    letter-spacing: 0.2px;
  }
  .variety-title--red { left: 38px; top: 64px; color: var(--ink); }
  .variety-title--white { right: 52px; top: 583px; color: var(--gold-heading); }

  .dimensions {
    position: absolute;
    left: 0; top: 0;
    width: 750px; height: 1200px;
    pointer-events: none;
  }
  .dimensions text {
    font-family: var(--plain);
    font-size: 9px;
    fill: var(--ink);
  }
  .dimensions line { stroke: var(--rule); stroke-width: 0.6; }

  .section-band {
    position: absolute;
    left: 0; top: 557px;
    width: 750px; height: 8px;
    background: var(--band);
  }

  .bottle {
    position: absolute;
    border-radius: 10px 10px 16px 16px;
  }
  .bottle--red {
    left: 585px; top: 22px; width: 118px; height: 508px;
    background: linear-gradient(90deg, #050505 0%, #1c1416 45%, #050505 100%);
  }
  .bottle--white {
    left: 38px; top: 578px; width: 115px; height: 512px;
    background: linear-gradient(180deg, #c9a94a 0%, #e9e2c2 24%, #f3eed8 60%, #e8e0bf 100%);
  }

  /* ---------- Front label ---------- */
  .front-label {
    position: absolute;
    width: 234px; height: 234px;
    padding: 7px;
  }
  .front-label__panel {
    position: relative;
    width: 100%; height: 100%;
    text-align: center;
  }
  .front-label__rule {
    position: absolute;
    inset: 8px;
    border: 1px solid currentColor;
    opacity: 0.7;
  }
  .front-label__stars {
    position: absolute; left: 0; right: 0; top: 19px;
    font-size: 6px; letter-spacing: 2px;
  }
  .front-label__mark {
    position: absolute;
    left: 50%; top: 40px;
    width: 46px; height: 46px;
    margin-left: -23px;
    border-radius: 50%;
    border: 3px solid currentColor;
    opacity: 0.75;
  }
  .front-label__brand {
    position: absolute; left: 0; right: 0; top: 99px;
    font-family: var(--sans);
    font-weight: 600;
    font-size: 16px;
    letter-spacing: 1px;
  }
  .front-label__vineyard {
    position: absolute; left: 0; right: 0; top: 139px;
    font-family: var(--script);
    font-size: 16px;
  }
  .front-label__year {
    position: absolute; left: 0; right: 0; top: 160px;
    font-family: var(--serif);
    font-size: 10.5px;
  }
  .front-label__variety {
    position: absolute; left: 0; right: 0; top: 176px;
    font-family: var(--plain);
    font-size: 12.5px;
    letter-spacing: 0.2px;
  }
  .front-label__region {
    position: absolute; left: 0; right: 0; top: 196px;
    font-family: var(--plain);
    font-size: 6.3px;
  }

  /* ---------- Back label ---------- */
  .back-label {
    position: absolute;
    width: 243px; height: 242px;
    border-radius: 6px;
    padding: 3px;
  }
  .back-label__panel {
    position: relative;
    width: 100%; height: 100%;
    border-radius: 4px;
  }
  .back-label__title-block {
    position: absolute; left: 6px; top: 14px; width: 112px;
    text-align: center;
  }
  .back-label__vineyard {
    font-family: var(--script);
    font-size: 12px;
    line-height: 12px;
    margin-left: -12px;
  }
  .back-label__year {
    font-family: var(--serif);
    font-size: 9px;
    line-height: 11px;
  }
  .back-label__variety {
    font-family: var(--sans);
    font-weight: 500;
    font-size: 9.6px;
    line-height: 13px;
    margin-top: 1px;
  }
  .back-label__appellation {
    font-family: var(--serif);
    font-size: 9.5px;
    line-height: 11px;
  }
  .back-label__brand-block {
    position: absolute; left: 148px; top: 14px; width: 82px;
    text-align: center;
  }
  .back-label__mark {
    display: block;
    width: 28px; height: 28px;
    margin: 0 auto 6px;
    border-radius: 50%;
    border: 2px solid currentColor;
    opacity: 0.8;
  }
  .back-label__brand {
    font-family: var(--sans);
    font-weight: 600;
    font-size: 8.5px;
    letter-spacing: 0.6px;
  }
  .back-label__story {
    position: absolute; left: 6px; right: 6px; top: 66px;
    font-family: var(--serif);
    font-size: 7.6px;
    line-height: 9.3px;
    text-align: center;
  }
  .back-label__notes {
    position: absolute; left: 14px; right: 14px; top: 116px;
    font-family: var(--serif);
    font-size: 5.7px;
    line-height: 7.3px;
    text-align: center;
  }
  .back-label__stars {
    position: absolute; left: 0; right: 0; top: 164px;
    text-align: center;
    font-size: 6px; letter-spacing: 2px;
  }
  .back-label__producer {
    position: absolute; left: 8px; right: 8px; top: 175px;
    text-align: center;
    font-family: var(--sans);
    font-weight: 600;
    font-size: 5.8px;
    letter-spacing: 1.9px;
  }
  .back-label__warning {
    position: absolute; left: 10px; right: 10px; top: 187px;
    font-family: var(--condensed);
    font-size: 6px;
    line-height: 8.3px;
    text-align: justify;
    text-align-last: justify;
  }
  .back-label__warning strong { font-weight: 700; }
  .back-label__facts {
    position: absolute; left: 10px; right: 10px; top: 226px;
    display: flex;
    justify-content: space-between;
    font-family: var(--condensed);
    font-size: 6px;
  }
  .back-label__facts span:nth-child(2) { margin-right: 36px; }

  /* ---------- Colourways ---------- */
  .label--silver { color: var(--silver-ink); }
  .front-label.label--silver {
    background: linear-gradient(135deg, var(--silver-frame-a) 0%, var(--silver-frame-b) 38%, var(--silver-frame-c) 62%, var(--silver-frame-a) 100%);
  }
  .label--silver .front-label__panel,
  .label--silver .back-label__panel { background: var(--silver-fill); }
  .back-label.label--silver { background: #a5a7ac; }

  .label--gold { color: var(--gold-ink); }
  .front-label.label--gold {
    background: linear-gradient(135deg, var(--gold-frame-a) 0%, var(--gold-frame-b) 38%, var(--gold-frame-c) 62%, var(--gold-frame-a) 100%);
  }
  .label--gold .front-label__panel,
  .label--gold .back-label__panel { background: var(--gold-fill); }
  .back-label.label--gold { background: #a48c3a; }

  .dieline-note {
    position: absolute;
    width: 100px;
    text-align: center;
    font-family: var(--plain);
    font-size: 9px;
    line-height: 11px;
  }

  .draft-note {
    position: absolute;
    left: 477px; top: 1122px;
    width: 273px; height: 61px;
    background: var(--band);
    color: #ffffff;
    padding: 6px 8px;
    font-family: var(--plain);
    font-size: 13.5px;
    line-height: 15px;
  }
</style>
</head>
<body>
<main class="sheet">

  <!-- Red wine section -->
  <h2 class="variety-title variety-title--red">CABERNET SAUVIGNON</h2>

  <svg class="dimensions" viewBox="0 0 750 1200" aria-hidden="true">
    <!-- red section -->
    <line x1="39" y1="137" x2="39" y2="155"/><line x1="520" y1="137" x2="520" y2="155"/>
    <line x1="41" y1="146" x2="250" y2="146"/><line x1="303" y1="146" x2="518" y2="146"/>
    <text x="276" y="149.5" text-anchor="middle">7.125"</text>
    <line x1="39" y1="170" x2="39" y2="188"/><line x1="271" y1="170" x2="271" y2="188"/><line x1="280" y1="170" x2="280" y2="188"/>
    <line x1="41" y1="179" x2="128" y2="179"/><line x1="182" y1="179" x2="269" y2="179"/>
    <line x1="283" y1="179" x2="295" y2="179"/>
    <text x="155" y="182.5" text-anchor="middle">3.500"</text>
    <text x="298" y="182.5">.125"</text>
    <line x1="528" y1="207" x2="546" y2="207"/><line x1="528" y1="440" x2="546" y2="440"/>
    <line x1="536" y1="209" x2="536" y2="314"/><line x1="536" y1="334" x2="536" y2="438"/>
    <text x="536" y="327.5" text-anchor="middle">3.500"</text>
    <line x1="396" y1="441" x2="396" y2="462"/><circle cx="396" cy="441" r="1.4" fill="#333"/>

    <!-- white section -->
    <line x1="205" y1="693" x2="205" y2="712"/><line x1="687" y1="693" x2="687" y2="712"/>
    <line x1="207" y1="702" x2="416" y2="702"/><line x1="470" y1="702" x2="685" y2="702"/>
    <text x="442" y="705.5" text-anchor="middle">7.125"</text>
    <line x1="205" y1="726" x2="205" y2="744"/><line x1="437" y1="726" x2="437" y2="744"/><line x1="446" y1="726" x2="446" y2="744"/>
    <line x1="207" y1="735" x2="294" y2="735"/><line x1="348" y1="735" x2="435" y2="735"/>
    <line x1="449" y1="735" x2="461" y2="735"/>
    <text x="321" y="738.5" text-anchor="middle">3.500"</text>
    <text x="464" y="738.5">.125"</text>
    <line x1="693" y1="763" x2="712" y2="763"/><line x1="693" y1="997" x2="712" y2="997"/>
    <line x1="702" y1="765" x2="702" y2="870"/><line x1="702" y1="890" x2="702" y2="995"/>
    <text x="702" y="883.5" text-anchor="middle">3.500"</text>
    <line x1="562" y1="998" x2="562" y2="1019"/><circle cx="562" cy="998" r="1.4" fill="#333"/>
  </svg>

  <section class="front-label label--silver" style="left:39px; top:208px;" aria-label="Cabernet Sauvignon front label">
    <div class="front-label__panel">
      <span class="front-label__rule"></span>
      <div class="front-label__stars">★★★</div>
      <span class="front-label__mark"></span>
      <div class="front-label__brand">BRINDOR RANCH</div>
      <div class="front-label__vineyard">Twin Rows Vineyard</div>
      <div class="front-label__year">2022</div>
      <div class="front-label__variety">CABERNET SAUVIGNON</div>
      <div class="front-label__region">PALOS VERDES PENINSULA</div>
    </div>
  </section>

  <section class="back-label label--silver" style="left:276px; top:203px;" aria-label="Cabernet Sauvignon back label">
    <div class="back-label__panel">
      <div class="back-label__title-block">
        <div class="back-label__vineyard">Twin Rows Vineyard</div>
        <div class="back-label__year">2022</div>
        <div class="back-label__variety">SAUVIGNON BLANC</div>
        <div class="back-label__appellation">California</div>
      </div>
      <div class="back-label__brand-block">
        <span class="back-label__mark"></span>
        <div class="back-label__brand">BRINDOR RANCH</div>
      </div>
      <p class="back-label__story">Nestled between French lavender and roses, riding arenas and horse pastures, and the serenity of Rolling Hills lies Twin Rows Vineyard. Established in 2014 at Larkspur Farm, a hobby farm owned by a mother and daughter, these 7 rows of Cabernet Sauvignon and 7 rows of Sauvignon Blanc are lovingly tended.</p>
      <p class="back-label__notes">The Cabernet Sauvignon, grown from the limestone rich hills of the Palos Verdes Peninsula, is well balanced with light acidity. Richly flavored and garnet colored, with a delicately spiced aroma, this wine brings forth ripe red fruit flavors of blackberry and cherry. A perfect compliment to a hearty barbecued steak or pasta.</p>
      <div class="back-label__stars">★★★</div>
      <div class="back-label__producer">PRODUCED &amp; BOTTLED BY BRINDOR RANCH, CA</div>
      <p class="back-label__warning"><strong>GOVERNMENT WARNING:</strong> (1) ACCORDING TO THE SURGEON GENERAL, WOMEN SHOULD NOT DRINK ALCOHOLIC BEVERAGES DURING PREGNANCY BECAUSE OF THE RISK OF BIRTH DEFECTS. (2) CONSUMPTION OF ALCOHOLIC BEVERAGES IMPAIRS YOUR ABILITY TO DRIVE A CAR OR OPERATE MACHINERY, AND MAY CAUSE HEALTH PROBLEMS.</p>
      <div class="back-label__facts"><span>CONTAINS SULFITES</span><span>ALC. 13.5% BY VOL</span><span>750 ML</span></div>
    </div>
  </section>

  <p class="dieline-note" style="left:346px; top:466px;">DIELINE DOES<br>NOT PRINT</p>

  <div class="bottle bottle--red" role="img" aria-label="Dark red wine bottle mock-up wearing the silver Cabernet Sauvignon front label"></div>

  <div class="section-band"></div>

  <!-- White wine section -->
  <div class="bottle bottle--white" role="img" aria-label="Clear bottle of pale white wine with gold capsule wearing the gold Sauvignon Blanc front label"></div>

  <h2 class="variety-title variety-title--white">SAUVIGNON BLANC</h2>

  <section class="front-label label--gold" style="left:205px; top:764px;" aria-label="Sauvignon Blanc front label">
    <div class="front-label__panel">
      <span class="front-label__rule"></span>
      <div class="front-label__stars">★★★</div>
      <span class="front-label__mark"></span>
      <div class="front-label__brand">BRINDOR RANCH</div>
      <div class="front-label__vineyard">Twin Rows Vineyard</div>
      <div class="front-label__year">2022</div>
      <div class="front-label__variety">SAUVIGNON BLANC</div>
      <div class="front-label__region">PALOS VERDES PENINSULA</div>
    </div>
  </section>

  <section class="back-label label--gold" style="left:442px; top:759px;" aria-label="Sauvignon Blanc back label">
    <div class="back-label__panel">
      <div class="back-label__title-block">
        <div class="back-label__vineyard">Twin Rows Vineyard</div>
        <div class="back-label__year">2022</div>
        <div class="back-label__variety">SAUVIGNON BLANC</div>
        <div class="back-label__appellation">California</div>
      </div>
      <div class="back-label__brand-block">
        <span class="back-label__mark"></span>
        <div class="back-label__brand">BRINDOR RANCH</div>
      </div>
      <p class="back-label__story">Nestled between French lavender and roses, riding arenas and horse pastures, and the serenity of Rolling Hills lies Twin Rows Vineyard. Established in 2014 at Larkspur Farm, a hobby farm owned by a mother and daughter, these 7 rows of Cabernet Sauvignon and 7 rows of Sauvignon Blanc are lovingly tended.</p>
      <p class="back-label__notes">The Sauvignon Blanc from the mist swept hill of the Palos Verdes Peninsula is sure to refresh any summer evening. Upon pouring a glass, you are greeted by waves of the aroma of citrus, infused with tropical flavors of luscious pineapple and guava. This light and crisp wine captures the coastal climate from which it was grown, perfectly suited for warm summer afternoons and al fresco dining.</p>
      <div class="back-label__stars">★★★</div>
      <div class="back-label__producer">PRODUCED &amp; BOTTLED BY BRINDOR RANCH, CA</div>
      <p class="back-label__warning"><strong>GOVERNMENT WARNING:</strong> (1) ACCORDING TO THE SURGEON GENERAL, WOMEN SHOULD NOT DRINK ALCOHOLIC BEVERAGES DURING PREGNANCY BECAUSE OF THE RISK OF BIRTH DEFECTS. (2) CONSUMPTION OF ALCOHOLIC BEVERAGES IMPAIRS YOUR ABILITY TO DRIVE A CAR OR OPERATE MACHINERY, AND MAY CAUSE HEALTH PROBLEMS.</p>
      <div class="back-label__facts"><span>CONTAINS SULFITES</span><span>ALC. 12.5% BY VOL</span><span>750 ML</span></div>
    </div>
  </section>

  <p class="dieline-note" style="left:512px; top:1023px;">DIELINE DOES<br>NOT PRINT</p>

  <aside class="draft-note">DRAFT 1:<br>First version for proof of concept<br>for the first round of feedback</aside>

</main>
</body>
</html>
```